Young adult personal development needs podcast 1400x1400 logo

We need artwork done for a podcast logo. The podcast is called The Brightmakers Show and is aimed at ages 20-30 waking up and wanting to make changes in their lives.

Using either of the two photos with the logo at bottom right of picture.

Somewhere it says: The Brightmakers Show: Educating & inspiring you to reach your greatest potential.

"The Brightmakers Show: Educating & inspiring you to reach your greatest potential.

With a strong belief in mentors and role models being a key factor to anyones success, Callum has placed himself along side the best in their fields.

Diving into movement, primal patterns, mindfulness, creativity and even the influence our gut has over our brain, these experts are going to show you how these pieces paint the picture that is your greatest potential."

```html
<!DOCTYPE html>
<html lang="en">
<head>
<meta charset="utf-8">
<title>The Brightmakers Show</title>
<link rel="stylesheet" href="https://fonts.googleapis.com/css2?family=Raleway:wght@700;800;900&display=swap">
<style>
  :root {
    --brand-blue: #0b65a6;
    --sky-top: #d9e0e5;
    --sky-low: #c9d1d7;
    --sea: #9fa9ac;
    --land: #56603f;
    --land-dark: #3f4a2e;
    --mark-white: #ffffff;
  }
  html, body {
    margin: 0;
    padding: 0;
    width: 1200px;
    height: 1200px;
    overflow: hidden;
  }
  .cover {
    position: relative;
    width: 1200px;
    height: 1200px;
    overflow: hidden;
    font-family: "Raleway", sans-serif;
  }
  .cover__photo {
    position: absolute;
    inset: 0;
    background: linear-gradient(
      to bottom,
      var(--sky-top) 0%,
      var(--sky-low) 68%,
      #b9c2c7 72%,
      var(--sea) 74%,
      #a4aeb1 83%,
      var(--land) 87%,
      var(--land-dark) 100%
    );
  }
  .title-frame {
    position: absolute;
    left: 127px;
    top: 249px;
    width: 947px;
    height: 320px;
    box-sizing: border-box;
    border: 3px solid var(--brand-blue);
    display: flex;
    align-items: center;
    justify-content: center;
  }
  .title {
    margin: 0;
    color: var(--brand-blue);
    font-weight: 900;
    font-size: 74px;
    line-height: 106px;
    text-align: center;
    letter-spacing: -0.5px;
    text-transform: uppercase;
  }
  .tagline {
    position: absolute;
    left: 0;
    right: 0;
    top: 628px;
    margin: 0;
    color: var(--brand-blue);
    font-weight: 700;
    font-size: 35px;
    line-height: 52px;
    text-align: center;
    text-transform: uppercase;
  }
  .brand-mark {
    position: absolute;
    right: 66px;
    top: 1100px;
    display: flex;
    align-items: center;
    gap: 12px;
    color: var(--mark-white);
    font-weight: 700;
    font-size: 26px;
    letter-spacing: 1px;
    text-transform: uppercase;
  }
  .brand-mark__dot {
    width: 18px;
    height: 18px;
    border-radius: 50%;
    background: var(--mark-white);
  }
</style>
</head>
<body>
  <main class="cover">
    <div class="cover__photo" role="img" aria-label="Photo from behind of a long-haired man with arms spread wide, standing on a green hilltop overlooking a grey sea under an overcast sky"></div>
    <div class="title-frame">
      <h1 class="title">The Brightmakers<br>Show</h1>
    </div>
    <p class="tagline">Educating &amp; inspiring you to reach<br>your greatest potential</p>
    <div class="brand-mark">
      <span class="brand-mark__dot"></span>
      <span class="brand-mark__name">Kestrel Potential</span>
    </div>
  </main>
</body>
</html>
```